Raw Food & Health Coach Needs a Clutch Coupon

I need a clutch coupon for a raw food & health coaching business based in Washington, DC called Maren Okafor, LLC. I help ladies and gents on the go who want to support their bodies to stay healthy or prevent/correct disease so they can live extraordinary lives while deeply serving the world. My services include individual coaching, (online) group coaching, and corporate wellness coaching.

I would like to create a clutch coupon to give to referral partners who in turn will give them to their clients. So far I have two referral partners in mind: Tobias Venn Salon & Spa; and Colon Hydrotherapist Greta Mulvane.

Tobias Venn Salon & Spa will be having an event on Thursday, September 12, 2013, during which time their clients who get a hair cut will receive a complimentary Plumetra (hair) Treatment & a complimentary Radiant Roots Forward Blueprint Session with me.

I would like to see designs that use 2-4 colors, including a bit of green. The final design should communicate beauty/health from the inside out and boundless energy to enjoy an extraordinary life. It should be natural yet elegant/classy.

Designers are currently working on my business logo. The logo design project has not yet been completed. Once it completes, I will send the logo design to you and request that you incorporate the logo into your coupon design.

IMPORTANT: I need to select a winning design on Wed, Sept 11, 2013, and get the source files from the designer within 24 hours (before Thursday, Sept 12 MORNING); so that I have time to adjust any text and take it to the printer in order to distribute the coupon later that afternoon. I will need the source files urgently (within the next 24 hours).

Then after the event the designer will make the changes on the design for me incorporating my logo for use with multiple referral partners. I will approve the Payment when I have finalized the design

To repeat, I must have the winning design on September 11 (or Sept 12 morning at the latest).

IMPORTANT: Refer to uploaded Referral Partner Clutch Coupon SAMPLE to give you an idea of the layout I'd like, but PLEASE don't let it stifle YOUR creativity.
Updates

The focus should be on the Free Radiant Roots Forward Blueprint Session, not on me.

 

I think I’d prefer a white background and black text, unless you can convince me otherwise by showing me a beautiful design.

 

Ensure there is space between paragraphs.

 

Somehow differentiate my free gift (Vital Shield Starter Kit), phone and URL at the bottom on the back. While it would be nice to include my free gift, I may have to leave out if it won’t fit on the coupon.

Reason: Not completely satisfied yet and open to more designs. Maren

Reason: Need more time and would like to see more designs.

Target Market(s)

The audience is busy, heart-centered/socially responsible professional men and women on the go who hardly have time for self-care, but who will pay for holistic services (alternative therapies) to enhance their beauty/health so that they can perform their best while deeply serving the world without getting sick or having to endure toxic therapies like surgery, chemotherapy, radiation, and pills.

Industry/Entity Type

Printer

Requirements
Must have
• 2-4 colors, including a little green

Dimensions: approx. 2.25 inches x 5.25 inches.

Text from the uploaded file. Note: I'm not sure if all the text I've provided will fit nicely on the back of the coupon. If no then please increase the dimensions as little as possible.

The front of the coupon designed horizontally, and the back designed vertically.
Nice to have
• I'm open to your using illustrations or photos of the raw food and/or lifestyle tools that I use with clients in my business, such as green juice, (leafy) green veggies, cucumbers, lemons, berries, green smoothies, superfoods, movement/exercise, self-care...

I also like the idea of including a face in the design. When I’ve surveyed in the past people have related better to a face than just to a bowl of veggies or fruit.
Should not have
• the colors orange or red, or florescent colors.

```html
<!DOCTYPE html>
<html lang="en">
<head>
<meta charset="utf-8">
<title>Maren Okafor, LLC – Clutch Coupon</title>
<link href="https://fonts.googleapis.com/css2?family=Source+Sans+3:wght@400;600;700&display=swap" rel="stylesheet">
<style>
:root{
  --stage:#cfcccc;
  --green:#1ea24b;
  --green-deep:#138a3c;
  --teal:#3fae8a;
  --photo-warm:#8f8a5a;
  --photo-soft:#b9c7a5;
  --white:#ffffff;
  --shadow:rgba(0,0,0,.28);
}
*{margin:0;padding:0;box-sizing:border-box}
html,body{width:1200px;height:800px;overflow:hidden}
body{background:var(--stage);font-family:"Source Sans 3",Arial,sans-serif;color:var(--white);position:relative}

.card{position:absolute;background:var(--green);box-shadow:2px 3px 8px var(--shadow);overflow:hidden}

/* Front */
.coupon-front{left:43px;top:61px;width:707px;height:303px}
.front-photo{position:absolute;left:0;top:0;width:360px;height:303px;
  background:linear-gradient(90deg,#7d9a86 0%,#a7b9a4 30%,#5fae86 70%,var(--green) 100%)}
.front-brand{position:absolute;left:89px;top:27px;font-size:17px;font-weight:700;letter-spacing:4px;white-space:nowrap}
.front-offer{position:absolute;left:362px;top:23px;width:320px}
.offer-title{font-size:22px;font-weight:600;letter-spacing:4px;border-bottom:2px solid var(--white);padding-bottom:1px;line-height:26px}
.offer-session{font-size:14px;line-height:18px;margin-top:5px}
.offer-length{font-size:16px;margin-top:27px;line-height:20px}
.offer-value{font-size:20px;font-weight:700;line-height:24px;margin-top:2px}
.offer-source{font-size:16px;line-height:20px;margin-top:28px}
.offer-link{font-size:16px;font-weight:700;line-height:22px}

/* Back */
.coupon-back{left:835px;top:58px;width:302px;height:707px}
.back-photo{position:absolute;left:0;top:0;width:302px;height:390px;
  background:linear-gradient(180deg,#7f8a5c 0%,var(--photo-warm) 20%,#6fa066 55%,var(--green) 100%)}
.back-content{position:absolute;left:25px;top:14px;width:252px;font-size:10.6px;line-height:13.4px}
.qa-title{font-size:17px;font-weight:700;letter-spacing:3px;border-bottom:2px solid var(--white);line-height:20px}
.qa-question{font-weight:700;font-size:11.2px;margin-top:2px}
.qa-question.caps{text-transform:uppercase;font-size:10.4px;margin-top:10px}
.qa-answer{text-align:justify}
.benefits{list-style:none;margin:15px 0 0 2px}
.benefits li{padding-left:24px;position:relative}
.benefits li::before{content:"»";position:absolute;left:0}
.qa-question.gap{margin-top:14px}
.coach-photo{position:absolute;left:25px;top:575px;width:117px;height:114px;
  background:linear-gradient(135deg,#5b4a3c,#a48872 55%,#7a6a55)}
.back-contact{position:absolute;left:158px;top:595px;font-size:10.6px;line-height:13.4px}
.back-contact strong{font-weight:700}
</style>
</head>
<body>

<section class="card coupon-front">
  <div class="front-photo" role="img" aria-label="Photo of a relaxed young man in a white shirt"></div>
  <div class="front-brand">MAREN OKAFOR, LLC</div>
  <div class="front-offer">
    <h1 class="offer-title">TREAT YOURSELF</h1>
    <p class="offer-session">Free Radiant Roots Forward Blueprint Session with Certified Raw Food &amp; Health Coach, Maren Okafor</p>
    <p class="offer-length">30 minutes, focused entirely on you.</p>
    <p class="offer-value">(A $50 VALUE, FREE)</p>
    <p class="offer-source">Compliments of Tobias Venn Salon &amp; Spa<br>To schedule your appointment, simply go to:</p>
    <p class="offer-link">HTTP://GO.MARENOK.CO/RRFB.</p>
  </div>
</section>

<section class="card coupon-back">
  <div class="back-photo" role="img" aria-label="Photo of a basket of fresh strawberries"></div>
  <div class="back-content">
    <h2 class="qa-title">Q. &amp; A.</h2>
    <p class="qa-question">What is Raw Food &amp; Health Coaching?</p>
    <p class="qa-answer">Raw food coaching helps you go or stay raw to the level that you truly desire. Health coaching helps you connect the dots between what you eat and how you feel. You'll know how to detoxify and oxygenate your body, alkalize your pH, and delight in what you eat like never before – without restriction.</p>
    <p class="qa-question caps">Who benefits from this work?</p>
    <p class="qa-answer">Smart, service-oriented ladies and gents on the go who want to enable their bodies to prevent/ correct disease and create energy so they can live extraordinary lives without crashing, getting sick or neglecting their own health. Raw food is literally for everyone, but the degree to which someone goes raw and for what duration is a very personal decision. This is about what works for you, what feels right for you and what get you to where you want to be. Generally speaking, raw food &amp; health coaching is great for anyone who wants to…</p>
    <ul class="benefits">
      <li>Correct or prevent a serious disease</li>
      <li>Look and/or feel better</li>
      <li>Look/feel 10 years younger</li>
      <li>Gravitate to their perfect body weight without dieting</li>
      <li>Double their energy</li>
      <li>Reduce their cravings</li>
      <li>Detox their body</li>
      <li>Think more clearly</li>
      <li>Get a lot done without having a lot of time</li>
      <li>Feel happier/improve their mood</li>
    </ul>
    <p class="qa-question gap">What happens in the initial consultation?</p>
    <p class="qa-answer">This 30 minute phone call is a time to discuss your unique health challenge(s) and desires. I guarantee you'll walk away with at least 1 aha about why you're stuck and more clarity about what it'll take to put you on the fast track to where you want to go.</p>
  </div>
  <div class="coach-photo" role="img" aria-label="Portrait photo of coach Maren Okafor"></div>
  <div class="back-contact">
    To schedule your<br>appointment, simply go<br>to: <strong>http://go.marenok.co/rrfb.</strong><br>
    <strong>202-555-0147</strong><br><strong>marenokafor.com</strong>
  </div>
</section>

</body>
</html>
```